Fresh & Clean *NEW* BUSINESS CARD Needed - OPTOMETRY Clinic/Optical

High-tech optometry practice with 3 doctors seeking new business card.  We provide eye exams, sell, designer glasses/contacts/specialty eyewear and treat ocular diseases.  For our business cards, we are seeking fresh, clean, and crisp design as we grow our team (staffing change).  Simply adding doctors is making the card look busy/cluttered.
 Looking for professional, less cluttered look yet still have our logo, doctor names, phone, address, and website....If possible!  :)
Names:
Marcia Trelford, O.D.
Ned Pallister, O.D.
Oona Ferrant, O.D.
Phone: 555-014-2738
Website: www.BrightLensHub.example
Address:  417 Garnet R. Holloway, Fernvale Crossing, FV 00000
Ultimately we have the main business card with all doctor sames and that card has two versions  (front is always the same).  The back has two designs (1) displays next appointment time/date, (2) for "general use" (non-appointment.)    I have attached what we have used in the past.  
We also need a design template for each team member in our practice with their name, title, and email.   Those should be designed with the "general use" back (see attached).
**Open to entirely new design so don't feel obligated to keep current format.  Need new perspective!  Also including our watermark and some other design features we have consistently used in past in our portfolio.  Included are two options for logos--vertical and horizontal.
**I also would like to remove "Member of Sight Alliance" on our logo if possible**
 Other image files available upon request.

Target Market(s)

New patient & Current Patients

Industry/Entity Type

Optometry

Contact Information for Business Card

High-tech optometry practice with 3 doctors seeking new business card.  We provide eye exams, sell, designer glasses/contacts/specialty eyewear and treat ocular diseases.  For our business cards, we are seeking fresh, clean, and crisp design as we grow our team (staffing change).  Simply adding doctors is making the card look busy/cluttered.  Looking for professional, less cluttered look yet still have our logo, doctor names, phone, address, and website....If possible!  :) Names: Marcia Trelford, O.D. Ned Pallister, O.D. Oona Ferrant, O.D. Phone: 555-014-2738 Website: www.BrightLensHub.example Address:  417 Garnet R. Holloway, Fernvale Crossing, FV 00000 Ultimately we have the main business card with all doctor sames and that card has two versions  (front is always the same).  The back has two designs (1) displays next appointment time/date, (2) for "general use" (non-appointment.)    I have attached what we have used in the past.   We also need a design template for each team member in our practice with their name, title, and email.   Those should be designed with the "general use" back (see attached). **Open to entirely new design so don't feel obligated to keep current format.  Need new perspective!  Also including our watermark and some other design features we have consistently used in past in our portfolio.  Included are two options for logos--vertical and horizontal. **I also would like to remove "Member of Sight Alliance" on our logo if possible**  Other image files available upon request.

Font styles to use
Other font styles liked:
• We have used Montserrat / Yellowtail in the past

Colors

Designer to choose colors to be used in the design.

Requirements
Must have
• Clean & Fresh Design with Logo / Info provided in description. Horizontal orientation. **I have included the CMYK colors we currently have in our logo.
Should not have
• Cluttered

```html
<!DOCTYPE html>
<html lang="en">
<head>
<meta charset="utf-8">
<title>BrightLens Hub – Business Card</title>
<link rel="stylesheet" href="https://fonts.googleapis.com/css2?family=Montserrat:wght@400;700&display=swap">
<style>
  :root {
    --backdrop: #e4e4e4;
    --card-white: #ffffff;
    --card-grey: #747577;
    --ink: #666769;
    --ink-soft: #6f7073;
    --gold: #d4a80c;
    --aqua: #a9d9e2;
    --white: #ffffff;
  }
  * { box-sizing: border-box; margin: 0; padding: 0; }
  html, body { width: 1200px; height: 1200px; overflow: hidden; }
  body {
    background: var(--backdrop);
    font-family: "Montserrat", Arial, sans-serif;
    position: relative;
  }
  .card {
    position: absolute;
    width: 700px;
    height: 400px;
  }
  .card--front { left: 253px; top: 131px; background: var(--card-white); }
  .card--back { left: 258px; top: 651px; background: var(--card-grey); }

  .brand-stack {
    position: absolute;
    left: 0; width: 336px; top: 0; height: 400px;
  }
  .brand-stack .brand-dot {
    position: absolute;
    left: 152px; top: 98px;
    width: 90px; height: 90px;
    border-radius: 50%;
    background: var(--aqua);
  }
  .brand-stack .brand-name {
    position: absolute;
    left: 0; width: 394px; top: 208px;
    text-align: center;
    font-size: 40px; font-weight: 400;
    line-height: 50px;
    color: var(--ink);
    letter-spacing: 1px;
  }
  .divider {
    position: absolute;
    left: 336px; top: 90px;
    width: 2px; height: 230px;
    background: linear-gradient(to bottom, rgba(102,103,105,0.15), rgba(102,103,105,0.7) 20%, rgba(102,103,105,0.7) 80%, rgba(102,103,105,0.15));
  }
  .details {
    position: absolute;
    left: 362px; top: 96px;
    color: var(--ink-soft);
  }
  .doctors { list-style: none; font-weight: 700; font-size: 20px; line-height: 24px; color: var(--ink); }
  .address { font-style: normal; font-size: 15.5px; line-height: 21.5px; margin-top: 16px; }
  .contact { list-style: none; font-size: 15.5px; line-height: 21px; margin-top: 10px; }
  .contact li { display: flex; align-items: center; gap: 10px; }
  .contact svg { width: 15px; height: 15px; flex: none; }

  .brand-row {
    position: absolute;
    left: 100px; top: 155px;
    display: flex; align-items: center; gap: 32px;
  }
  .brand-row .brand-dot {
    width: 84px; height: 84px; border-radius: 50%;
    background: var(--aqua);
  }
  .brand-row .brand-name {
    font-size: 42px; font-weight: 400; color: var(--white); letter-spacing: 1px;
  }
</style>
</head>
<body>
  <section class="card card--front" aria-label="Card front">
    <div class="brand-stack">
      <span class="brand-dot"></span>
      <p class="brand-name">brightlens<br>hub</p>
    </div>
    <span class="divider"></span>
    <div class="details">
      <ul class="doctors">
        <li>Marcia Trelford, O.D.</li>
        <li>Ned Pallister, O.D.</li>
        <li>Oona Ferrant, O.D.</li>
      </ul>
      <address class="address">417 Garnet R. Holloway<br>Fernvale Crossing, FV 00000</address>
      <ul class="contact">
        <li>
          <svg viewBox="0 0 24 24" aria-hidden="true"><path fill="var(--gold)" d="M6.6 10.8a15.1 15.1 0 0 0 6.6 6.6l2.2-2.2c.3-.3.7-.4 1-.2 1.1.4 2.3.6 3.6.6.6 0 1 .4 1 1V20c0 .6-.4 1-1 1A17 17 0 0 1 3 4c0-.6.4-1 1-1h3.5c.6 0 1 .4 1 1 0 1.3.2 2.5.6 3.6.1.3 0 .7-.2 1z"/></svg>
          555-014-2738
        </li>
        <li>
          <svg viewBox="0 0 24 24" aria-hidden="true"><circle cx="12" cy="12" r="10" fill="var(--gold)"/><path fill="var(--white)" d="M8 6c2 1 3 3 2 5-1 1-3 1-3 3 0 1 1 2 1 4-2-1-4-4-4-6 0-3 2-5 4-6zm7 4c2 0 3 2 2 4l-2 3c-1-1-2-2-1-4 0-1-1-2 1-3z"/></svg>
          www.BrightLensHub.example
        </li>
      </ul>
    </div>
  </section>

  <section class="card card--back" aria-label="Card back">
    <div class="brand-row">
      <span class="brand-dot"></span>
      <p class="brand-name">brightlens hub</p>
    </div>
  </section>
</body>
</html>
```